Newspaper ad for web design services

I have a paid space in a local newspaper size: 4.5085" W x 2.6875" H.
I want to use it for promoting my web design services.
Designers have the freedom to design the ad and the offer.
The goal is to have people contact me for business web design.
I published one ad last month and it totally failed to bring any attention.
Feel free to change or add anything you think can be more effective to attract potential customers (I can create any tripwire you consider will work)
Target: Houston-based business owners looking to get a new website or to update their existing one.

```html
<!DOCTYPE html>
<html lang="en">
<head>
<meta charset="utf-8">
<title>Corvo Designs – Newspaper Ad</title>
<link rel="stylesheet" href="https://fonts.googleapis.com/css2?family=Lato:wght@400;700;900&display=swap">
<style>
  :root {
    --page-bg: #efefef;
    --white: #ffffff;
    --ink: #1b1f36;
    --navy: #1e2a5e;
    --navy-light: #3a4a8c;
    --sky: #b7cbf5;
    --blue: #1f5ae8;
    --blue-deep: #1c2a66;
    --pink: #e56de6;
    --glow: #6fd0ff;
  }
  * { box-sizing: border-box; margin: 0; padding: 0; }
  html, body { width: 1200px; height: 1200px; overflow: hidden; background: var(--page-bg); }
  .canvas { position: relative; width: 1200px; height: 1200px; }

  .ad {
    position: absolute;
    left: 40px; top: 266px;
    width: 890px; height: 530px;
    transform: scale(1.2584);
    transform-origin: 0 0;
    overflow: hidden;
    background: var(--sky);
    font-family: "Lato", sans-serif;
  }
  .ad-shapes { position: absolute; inset: 0; width: 890px; height: 530px; }

  .brand { position: absolute; left: 40px; top: 26px; display: flex; align-items: center; gap: 12px; }
  .brand-mark { width: 44px; height: 44px; border-radius: 8px; background: var(--blue); }
  .brand-name { font-size: 34px; font-weight: 700; color: var(--ink); line-height: 1; }

  .headline { position: absolute; left: 35px; top: 98px; font-weight: 900; text-transform: uppercase; line-height: 1; }
  .headline-top { display: block; font-size: 30px; color: var(--white); letter-spacing: 0.2px; }
  .headline-main { display: block; font-size: 39px; color: var(--pink); margin-top: 6px; }

  .offer { position: absolute; left: 23px; top: 260px; width: 182px; text-align: center; color: var(--ink); }
  .offer-lead { font-size: 25px; font-weight: 400; line-height: 1; }
  .offer-badge { margin-top: 9px; height: 50px; background: var(--navy); color: var(--pink);
                 font-size: 38px; font-weight: 900; line-height: 50px; }
  .offer-item { margin-top: 10px; font-size: 31px; font-weight: 900; line-height: 1; }

  .showcase { position: absolute; left: 252px; top: 230px; width: 356px; height: 214px;
              border-radius: 6px;
              background: linear-gradient(135deg, #e8ecfb 0%, #9fb2ea 55%, #e56de6 100%); }

  .benefits { position: absolute; right: 20px; top: 150px; list-style: none; }
  .benefit { display: flex; align-items: center; justify-content: flex-end; gap: 10px; height: 62px; }
  .benefit-text { text-align: right; color: var(--white); font-size: 18px; font-weight: 400;
                  text-transform: uppercase; line-height: 21px; }
  .benefit-icon { width: 44px; height: 36px; display: flex; align-items: center; justify-content: center; }
  .benefit-dollar { color: var(--pink); font-size: 36px; font-weight: 700; line-height: 1; }

  .visit-label { position: absolute; left: 0; top: 460px; width: 130px; height: 70px;
                 line-height: 70px; text-align: center; color: var(--white); font-size: 30px; font-weight: 900; }
  .web-address { position: absolute; left: 292px; top: 460px; height: 70px; line-height: 70px;
                 color: var(--white); font-size: 30px; font-weight: 700; }
</style>
</head>
<body>
<div class="canvas">
  <section class="ad">
    <svg class="ad-shapes" viewBox="0 0 890 530" aria-hidden="true">
      <defs>
        <linearGradient id="band-gradient" x1="0" y1="0" x2="1" y2="0">
          <stop offset="0" stop-color="#1e2a5e"/>
          <stop offset="1" stop-color="#3a4a8c"/>
        </linearGradient>
        <linearGradient id="panel-gradient" x1="0" y1="0" x2="0" y2="1">
          <stop offset="0" stop-color="#2258e8"/>
          <stop offset="0.55" stop-color="#1f3b9c"/>
          <stop offset="1" stop-color="#1c2a66"/>
        </linearGradient>
        <linearGradient id="glow-line" x1="0" y1="0" x2="1" y2="0">
          <stop offset="0" stop-color="#6fd0ff" stop-opacity="0"/>
          <stop offset="0.5" stop-color="#6fd0ff"/>
          <stop offset="1" stop-color="#6fd0ff" stop-opacity="0"/>
        </linearGradient>
      </defs>
      <!-- header strip -->
      <rect x="0" y="0" width="890" height="83" fill="#ffffff"/>
      <!-- headline band -->
      <polygon points="0,83 740,83 680,195 0,195" fill="url(#band-gradient)"/>
      <rect x="90" y="179" width="330" height="2" fill="url(#glow-line)"/>
      <!-- bottom band -->
      <rect x="0" y="460" width="890" height="70" fill="#1f5ae8"/>
      <polygon points="0,460 132,460 158,495 132,530 0,530" fill="#e56de6"/>
      <polygon points="140,460 160,460 186,495 160,530 140,530 166,495" fill="#1e2a5e"/>
      <polygon points="168,460 222,460 262,495 222,530 168,530 194,495" fill="#ffffff"/>
      <g fill="none" stroke="#1e2a5e" stroke-width="2">
        <circle cx="220" cy="495" r="11"/>
        <ellipse cx="220" cy="495" rx="5" ry="11"/>
        <line x1="209" y1="495" x2="231" y2="495"/>
      </g>
      <!-- right benefits panel -->
      <polygon points="770,0 632,262 758,530 890,530 890,0" fill="#ffffff"/>
      <polygon points="788,0 646,262 776,530 890,530 890,0" fill="#e56de6"/>
      <polygon points="798,0 657,262 786,530 890,530 890,0" fill="url(#panel-gradient)"/>
    </svg>

    <div class="brand">
      <span class="brand-mark"></span>
      <span class="brand-name">Corvo Designs</span>
    </div>

    <h1 class="headline">
      <span class="headline-top">Make your business website</span>
      <span class="headline-main">Double your sales!</span>
    </h1>

    <div class="offer">
      <p class="offer-lead">Download Our</p>
      <p class="offer-badge">FREE</p>
      <p class="offer-item">E-BOOK</p>
    </div>

    <div class="showcase" role="img" aria-label="Illustration of a desktop monitor showing a website layout, with a video thumbnail of the web designer beside it"></div>

    <ul class="benefits">
      <li class="benefit">
        <span class="benefit-text">Get more<br>customers</span>
        <span class="benefit-icon">
          <svg width="44" height="32" viewBox="0 0 44 32" aria-hidden="true" fill="#e56de6">
            <circle cx="10" cy="9" r="5"/><circle cx="34" cy="9" r="5"/><circle cx="22" cy="8" r="6.5"/>
            <path d="M1 28c0-7 4-11 9-11s7 2 8 4v7z"/><path d="M43 28c0-7-4-11-9-11s-7 2-8 4v7z"/>
            <path d="M11 30c0-9 5-14 11-14s11 5 11 14z"/>
          </svg>
        </span>
      </li>
      <li class="benefit">
        <span class="benefit-text">Increase<br>sales</span>
        <span class="benefit-icon"><span class="benefit-dollar">$</span></span>
      </li>
      <li class="benefit">
        <span class="benefit-text">Refer more<br>customers</span>
        <span class="benefit-icon">
          <svg width="36" height="36" viewBox="0 0 36 36" aria-hidden="true">
            <path d="M24 8 A13 13 0 1 1 10 9" fill="none" stroke="#e56de6" stroke-width="4"/>
            <polygon points="4,4 16,6 8,15" fill="#e56de6"/>
          </svg>
        </span>
      </li>
      <li class="benefit">
        <span class="benefit-text">Get more<br>reviews</span>
        <span class="benefit-icon">
          <svg width="36" height="36" viewBox="0 0 36 36" aria-hidden="true">
            <polygon points="18,1 22.5,13 35,13 25,21 29,34 18,26 7,34 11,21 1,13 13.5,13" fill="#e56de6"/>
          </svg>
        </span>
      </li>
    </ul>

    <p class="visit-label">VISIT</p>
    <p class="web-address">www.corvo-designs.com</p>
  </section>
</div>
</body>
</html>
```